Web design and coding for Harbor Lantern

We are a consultancy specialising in contact centre services. Our target audience is organisations who have inhouse contact centres, outsource contact centre services and require services such as knowledge management, advisory, workforce management and training/OD.

Our purpose is 'We create customer experience heroes' and our tagline is 'Creating customer experience heroes'. Our vision "Asia Pacific's most Trusted Advisor in Customer Experience and Service Operations"

We need a website refresh - one that appeals to our target audience , captures our purpose and as well as our purpose. The website would support our marketing and direct sales and imagery should reflect our purpose, vision and appeal to our target market.

The website needs to be able to showcase our team (profiles) and case studies with the option of posting videos / articles /newsletters as well. Potential for capturing customer details would also be considered.
There may be some other ideas you have which we would also be open to.
Logo should remain as is (see Messaging House). Values are internal .

We will need the ability to update the website (using Wordpress) so design should cater for this.
Updates

Hi All Thanks for your submissions - we are reviewing designs early next week.

Hi Designers Thank you for your submissions. We've had a little delay due to COVID 19 work restrictions in selecting the design. We are hoping to make a decision by the end of the month. I'm sorry for the delay and will keep you updated. Thank you!

Target Market(s)

Asia Pac Business decision makers with Contact Centres - COOs, Knowledge Managers, Head of of L&D, Head of Workforce, GM Operations

Coding

Coded - Design and coding required

Number of Pages Required

5+ page

Colors
34a7d8
85acd3

Requirements
Must have
• See messaging house - HL colours should be used.
Nice to have
• Area for case studies and bios
Area for newsletters / posts
Should not have
• Values are internal - this gives the feel of the company rather than needing to be promoted.

```html
<!DOCTYPE html>
<html lang="en">
<head>
<meta charset="utf-8">
<title>Harbor Lantern — Creating Customer Experience Heroes</title>
<link href="https://fonts.googleapis.com/css2?family=Open+Sans:wght@400;600;700;800&display=swap" rel="stylesheet">
<style>
:root{
  --blue:#1b8fd6;
  --blue-dark:#0d6fb3;
  --orange:#ff5b0d;
  --ink:#1c1c1c;
  --muted:#8a8a8a;
  --white:#ffffff;
  --footer:#0b0b0b;
  --photo-cool-a:#cfd6df;
  --photo-cool-b:#4b5560;
  --photo-night-a:#1f3a5a;
  --photo-night-b:#0d1a2b;
}
*{box-sizing:border-box;margin:0;padding:0}
html,body{width:1200px;height:4808px;overflow:hidden}
body{position:relative;font-family:"Open Sans",Arial,sans-serif;color:var(--ink);background:var(--white)}
.abs{position:absolute}
.photo{position:absolute}
.btn{position:absolute;display:flex;align-items:center;justify-content:center;background:var(--orange);color:var(--white);font-size:15px;font-weight:600;border-radius:24px;height:40px}
.body-text{font-size:15.5px;line-height:26px;color:var(--muted)}

/* header */
.site-header{left:0;top:0;width:1200px;height:76px;background:var(--white);z-index:2}
.brand{left:88px;top:16px;display:flex;align-items:center;gap:12px;font-size:30px;font-weight:700;color:var(--blue)}
.brand-dot{width:30px;height:30px;border-radius:50%;background:var(--blue)}
.main-nav{left:492px;top:26px;display:flex;gap:36px;font-size:17px;font-weight:600}
.main-nav a{color:var(--ink);text-decoration:none;position:relative}
.main-nav a.active{color:var(--blue)}
.main-nav a.active::after{content:"";position:absolute;left:50%;top:28px;width:8px;height:8px;margin-left:-4px;border-radius:50%;background:var(--blue)}

/* hero */
.hero-photo{left:0;top:0;width:1200px;height:664px;background:radial-gradient(circle at 30% 30%,#f3e6d8 0%,#d9c0a5 40%,#9a7b5e 75%,#6a5240 100%)}
.hero-title{left:0;top:270px;width:1200px;text-align:center;font-size:50px;line-height:54px;font-weight:800;color:var(--ink);letter-spacing:1px}
.hero-btn{left:504px;top:400px;width:188px;height:52px;border-radius:26px;font-size:17px}
.hero-dots{left:0;top:628px;width:1200px;display:flex;justify-content:center;gap:10px}
.hero-dots span{width:10px;height:10px;border-radius:50%;background:rgba(255,255,255,.6)}
.hero-dots span.on{background:var(--white)}

/* bands */
.band{left:0;width:1200px;display:flex;align-items:center}
.band-title{position:absolute;left:88px;font-size:46px;font-weight:800;color:var(--white)}
.band-text{position:absolute;left:452px;font-size:21px;line-height:30px;font-weight:700;color:var(--white)}
.vision-band{top:668px;height:144px;background:var(--blue)}
.purpose-band{top:2568px;height:168px;background:var(--orange)}

/* split sections */
.round-photo{border-radius:50%}
.section-title{font-size:40px;font-weight:700;color:var(--ink)}

/* services */
.service-tile{top:1520px;width:300px;height:332px;overflow:hidden}
.service-label{position:absolute;left:14px;bottom:10px;font-size:19px;line-height:22px;font-weight:700;color:var(--white)}

/* team */
.member{top:2908px;width:280px;text-align:center}
.member-photo{width:216px;height:216px;border-radius:50%;margin:0 auto}
.member-name{margin-top:18px;font-size:19px;font-weight:600}
.member-role{font-size:13px;color:var(--muted)}

/* blog */
.blog{left:0;top:3304px;width:1200px;height:912px;background:var(--blue)}
.blog-title{left:0;top:100px;width:1200px;text-align:center;font-size:40px;font-weight:700;color:var(--white)}
.post{top:160px;width:504px;height:676px;background:var(--white)}
.post-photo{left:0;top:0;width:504px;height:384px}
.play{left:222px;top:162px}
.post-date{left:20px;top:280px;width:104px;height:104px;background:var(--blue);color:var(--white);text-align:center}
.post-date b{display:block;font-size:42px;line-height:56px;margin-top:10px}
.post-date span{font-size:15px}
.post-heading{left:0;top:406px;width:504px;font-size:24px;line-height:32px;font-weight:700}
.post-text{left:0;top:490px;width:504px;font-size:14px;line-height:20px}
.post .btn{left:0;top:604px;width:176px}

/* newsletter */
.newsletter{left:0;top:4216px;width:1200px;height:208px;background:var(--blue-dark)}
.newsletter-title{left:88px;top:52px;font-size:38px;line-height:46px;font-weight:800;color:var(--white)}
.newsletter-input{left:464px;top:64px;width:496px;height:44px;background:var(--white);font-size:14px;color:var(--muted);padding:12px 18px}
.newsletter-btn{left:960px;top:64px;width:152px;height:44px;background:var(--orange);color:var(--white);font-size:16px;font-weight:600;display:flex;align-items:center;justify-content:center}

/* footer */
.site-footer{left:0;top:4424px;width:1200px;height:384px;background:var(--footer);color:var(--white)}
.footer-col{top:48px}
.footer-col h4{font-size:23px;font-weight:600;margin-bottom:22px}
.footer-col li{list-style:none;font-size:15.5px;line-height:30px}
.copyright{left:0;top:324px;width:1200px;text-align:center;font-size:13px;border-top:1px solid #2a2a2a;padding-top:20px}
</style>
</head>
<body>

<div class="photo hero-photo" role="img" aria-label="Hand placing the fifth of five wooden stars on a row, soft bokeh background"></div>

<header class="abs site-header">
  <div class="abs brand"><span class="brand-dot"></span>Harbor Lantern</div>
  <nav class="abs main-nav">
    <a class="active" href="#">Home</a><a href="#">About Us</a><a href="#">Services</a><a href="#">Vision</a><a href="#">Team</a><a href="#">Blog</a><a href="#">Contact Us</a>
  </nav>
</header>

<h1 class="abs hero-title">CREATING CUSTOMER<br>EXPERIENCE HEROES</h1>
<a class="btn hero-btn">Get Started</a>
<div class="abs hero-dots"><span class="on"></span><span></span><span></span><span></span></div>

<section class="abs band vision-band">
  <h2 class="band-title">VISION</h2>
  <p class="band-text">Asia Pacific's Most Trusted Advisor In Customer<br>Experience and Service Operations</p>
</section>

<section class="about">
  <div class="photo round-photo" style="left:90px;top:926px;width:484px;height:484px;background:linear-gradient(135deg,var(--photo-cool-a),var(--photo-cool-b))" role="img" aria-label="Business meeting with a presenter in an office"></div>
  <h2 class="abs section-title" style="left:628px;top:950px">About Us</h2>
  <p class="abs body-text" style="left:628px;top:1030px;width:500px">Lorem ipsum dolor sit amet, consectetur adipiscing elit, sed do eiusmod tempor incididunt ut labore et dolore magna aliqua. Ut enim ad minim veniam, quis nostrud exercitation ullamco laboris nisi ut aliquip ex ea commodo consequat. Duis aute irure dolor in reprehenderit in voluptate velit esse cillum dolore eu fugiat nulla pariatur. Excepteur sint occaecat cupidatat non proident, sunt in culpa qui officia deserunt mollit anim id est laborum.</p>
  <a class="btn" style="left:628px;top:1324px;width:176px">Read More</a>
</section>

<section class="services">
  <div class="photo service-tile" style="left:0;background:linear-gradient(160deg,#c9b59f,#4a4038)" role="img" aria-label="Colleagues talking in a bright office"><span class="service-label">Customer Management<br>Consulting</span></div>
  <div class="photo service-tile" style="left:300px;background:radial-gradient(circle at 50% 40%,#e8b86a,#3a2a1c 70%)" role="img" aria-label="Hand holding a glowing light bulb"><span class="service-label">Knowledge<br>Management</span></div>
  <div class="photo service-tile" style="left:600px;background:linear-gradient(160deg,#d8c7b3,#5c4b3e)" role="img" aria-label="Training workshop with people seated around a table"><span class="service-label">Training &amp; Organisational<br>Development</span></div>
  <div class="photo service-tile" style="left:900px;background:linear-gradient(160deg,#c4c9ce,#3f464d)" role="img" aria-label="Hand touching gear icons on a grey background"><span class="service-label">Contact Centre<br>Optimisation</span></div>
</section>

<section class="case-studies">
  <h2 class="abs section-title" style="left:88px;top:1998px">Case Studies</h2>
  <p class="abs body-text" style="left:88px;top:2066px;width:470px">Lorem ipsum dolor sit amet, consectetur adipiscing elit, sed do eiusmod tempor incididunt ut labore et dolore magna aliqua. Ut enim ad minim veniam, quis nostrud exercitation ullamco laboris nisi ut aliquip ex ea commodo consequat. Duis aute irure dolor in reprehenderit in voluptate velit esse cillum dolore eu fugiat nulla pariatur. Excepteur sint occaecat cupidatat non proident, sunt in culpa qui officia deserunt mollit anim id est laborum.</p>
  <a class="btn" style="left:88px;top:2366px;width:176px">Read More</a>
  <div class="photo round-photo" style="left:626px;top:1970px;width:484px;height:484px;background:linear-gradient(135deg,#dfe3e8,#2b2f3a)" role="img" aria-label="Business people reviewing documents on a tablet"></div>
</section>

<section class="abs band purpose-band">
  <h2 class="band-title">PURPOSE</h2>
  <p class="band-text">We Create Customer Experience Heroes</p>
</section>

<section class="team">
  <h2 class="abs section-title" style="left:0;top:2836px;width:1200px;text-align:center">Our Team</h2>
  <div class="abs member" style="left:88px"><div class="member-photo" style="background:linear-gradient(135deg,#d9b59a,#7a5a44)" role="img" aria-label="Portrait of Mara Quinn"></div><div class="member-name">Mara Quinn</div><div class="member-role">Lorem ipsum dolor sit amet</div></div>
  <div class="abs member" style="left:350px"><div class="member-photo" style="background:linear-gradient(135deg,#d8d8d8,#6b6b6b)" role="img" aria-label="Portrait of Tobias Reed"></div><div class="member-name">Tobias Reed</div><div class="member-role">Lorem ipsum dolor sit amet</div></div>
  <div class="abs member" style="left:596px"><div class="member-photo" style="background:linear-gradient(135deg,#cfb9a3,#5e4a3a)" role="img" aria-label="Portrait of Leon Marsh"></div><div class="member-name">Leon Marsh</div><div class="member-role">Lorem ipsum dolor sit amet</div></div>
  <div class="abs member" style="left:860px"><div class="member-photo" style="background:linear-gradient(135deg,#dcdcdc,#5a5a5a)" role="img" aria-label="Portrait of Owen Price"></div><div class="member-name">Owen Price</div><div class="member-role">Lorem ipsum dolor sit amet</div></div>
</section>

<section class="abs blog">
  <h2 class="abs blog-title">Blog</h2>
  <article class="abs post" style="left:88px">
    <div class="photo post-photo" style="background:linear-gradient(135deg,#ece7df,#9b8e80)" role="img" aria-label="Hands sketching a plan with markers on paper"></div>
    <svg class="abs play" width="60" height="60" viewBox="0 0 60 60"><circle cx="30" cy="30" r="27" fill="none" stroke="#fff" stroke-width="4"/><path d="M24 18 L42 30 L24 42 Z" fill="#fff"/></svg>
    <div class="abs post-date"><b>25</b><span>oct 2020</span></div>
    <h3 class="abs post-heading">Lorem ipsum dolor sit amet, consectetur adipiscing elit, sed do eiusmod</h3>
    <p class="abs post-text body-text">Lorem ipsum dolor sit amet, consectetur adipiscing elit, sed do eiusmod tempor incididunt ut labore et dolore magna aliqua. Ut enim ad minim veniam, quis nostrud exercitation ullamco laboris nisi ut aliquip ex ea commodo consequat.</p>
    <a class="btn">Read More</a>
  </article>
  <article class="abs post" style="left:608px">
    <div class="photo post-photo" style="background:linear-gradient(135deg,var(--photo-night-a),var(--photo-night-b))" role="img" aria-label="Hand touching glowing network icons on a dark blue screen"></div>
    <svg class="abs play" width="60" height="60" viewBox="0 0 60 60"><circle cx="30" cy="30" r="27" fill="none" stroke="#fff" stroke-width="4"/><path d="M24 18 L42 30 L24 42 Z" fill="#fff"/></svg>
    <div class="abs post-date"><b>25</b><span>oct 2020</span></div>
    <h3 class="abs post-heading">Lorem ipsum dolor sit amet, consectetur adipiscing elit, sed do eiusmod</h3>
    <p class="abs post-text body-text">Lorem ipsum dolor sit amet, consectetur adipiscing elit, sed do eiusmod tempor incididunt ut labore et dolore magna aliqua. Ut enim ad minim veniam, quis nostrud exercitation ullamco laboris nisi ut aliquip ex ea commodo consequat.</p>
    <a class="btn">Read More</a>
  </article>
</section>

<section class="abs newsletter">
  <h2 class="abs newsletter-title">SUBSCRIBE OUR<br>NEWSLETTER</h2>
  <div class="abs newsletter-input">Enter Your Email Address</div>
  <div class="abs newsletter-btn">Subscribe</div>
</section>

<footer class="abs site-footer">
  <div class="abs footer-col" style="left:88px"><h4>Links</h4><ul><li>Home</li><li>About Us</li><li>Services</li><li>Vision</li><li>Team</li><li>Blog</li><li>Contact Us</li></ul></div>
  <div class="abs footer-col" style="left:364px"><h4>Others</h4><ul><li>FAQ</li><li>Privacy Police</li><li>Terms &amp; Conditions</li><li>Sitemap</li></ul></div>
  <div class="abs footer-col" style="left:640px"><h4>Contact Us</h4><ul><li>Lorem ipsum dolor sit amet,</li><li>consectetur adipiscing</li><li>+0 000 000 000</li><li>info@harborlantern.example</li></ul></div>
  <div class="abs footer-col" style="left:1004px"><h4>Follow Us</h4><ul><li>Newsroom</li><li>Updates</li><li>Network</li><li>Video Hub</li></ul></div>
  <p class="abs copyright">© 2021 Company Name | All Rights Reserved</p>
</footer>

</body>
</html>
```